Coming Soon page for a new fitness startup

We are a new startup based in Toronto, Canada working on a site and mobile app where people can register for athletic events such as running, cycling, triathlon, SUP, etc.

Participants will also be able to manage their clubs and team, and connect their fitness trackers so they have all their fitness data and friends in one place.

I like very simple designs and lots of whitespace. So no need for icons or unnecessary graphics.

I prefer having a mobile phone app instead of a hero image. No need to worry about the details within the mobile app for now, we can fill it in later. Here are some landing pages that I like.
https://pixelvault.example/torvanmelk/buckets/438197-Landing-Page

Attached is a wireframe that gives some sample content for each of the sections. Please do not take the wireframe too literally, it is only meant to illustrate the content that we are experimenting with and should give an idea of how much text will be on the page.

I have also attached the company logo files. The logo is not being used yet so feel free to simplify the logo if it doesn't look great with your design. For example, I'm ok with just the name "k7ravi" in white if that looks better.

Target Market(s)

Ages 25 to 45. Interested in running, cycling, triathlon, SUP, etc.

Industry/Entity Type

Fitness

Coding

Coded - Design and coding required

Number of Pages Required

1 page

Requirements
Should not have
• Any photos should not contain track and field events, or people in a gym. Any photos should have people running or cycling outdoors. I know that photos can be easily swapped out but it is distracting to review a design that has the wrong photos.

```html
<!DOCTYPE html>
<html lang="en">
<head>
<meta charset="utf-8">
<title>k7ravi — Coming Soon</title>
<link rel="stylesheet" href="https://fonts.googleapis.com/css2?family=Roboto:wght@300;400;500&display=swap">
<style>
  :root {
    --brand-red: #d31f34;
    --ink: #3d3d3d;
    --ink-soft: #555555;
    --muted: #8a8a8a;
    --line: #cfcfcf;
    --panel: #f3f3f3;
    --white: #ffffff;
    --icon: #4a4a4a;
    --phone-tone: #e9e9e9;
    --photo-tone-a: #c9d3e4;
    --photo-tone-b: #efe9e4;
  }
  * { box-sizing: border-box; margin: 0; padding: 0; }
  html, body {
    width: 1200px; height: 625px; overflow: hidden;
    background: var(--white);
    font-family: "Roboto", Arial, sans-serif;
    color: var(--ink);
  }
  .page { position: relative; width: 1200px; height: 625px; }

  /* Header */
  .site-header {
    position: absolute; left: 0; top: 0; width: 1200px; height: 91px;
    border-bottom: 1px solid #e6e6e6;
    box-shadow: 0 1px 3px rgba(0,0,0,0.06);
    background: var(--white);
  }
  .social { position: absolute; display: flex; gap: 2px; }
  .social span {
    display: block; width: 22px; height: 22px; border-radius: 50%;
    background: var(--icon);
  }
  .site-header .social { left: 7px; top: 38px; }
  .wordmark {
    position: absolute; left: 510px; top: 12px; height: 66px;
    display: flex; align-items: center; gap: 10px;
  }
  .wordmark-dot {
    width: 40px; height: 40px; border-radius: 50%; background: var(--brand-red);
  }
  .wordmark-name {
    font-size: 44px; font-weight: 500; color: var(--ink-soft); letter-spacing: 1px;
  }
  .launch-note {
    position: absolute; right: 14px; top: 40px;
    font-size: 13px; letter-spacing: 0.5px; color: var(--ink-soft);
  }

  /* Left: community */
  .community { position: absolute; left: 0; top: 91px; width: 600px; height: 475px; }
  .headline {
    position: absolute; font-size: 21px; font-weight: 300; color: var(--brand-red);
    letter-spacing: 0.3px; white-space: nowrap;
  }
  .community .headline { left: 9px; top: 21px; }
  .subhead {
    position: absolute; font-size: 12px; font-weight: 500; letter-spacing: 0.4px;
    color: var(--ink); line-height: 16px;
  }
  .body-copy {
    position: absolute; font-size: 10.5px; line-height: 15px; letter-spacing: 0.3px;
    color: var(--ink-soft);
  }
  .community .intro-title { left: 10px; top: 66px; }
  .community .intro-text { left: 10px; top: 101px; width: 320px; }
  .community .signup-title { left: 10px; top: 236px; width: 330px; }
  .notify-form {
    position: absolute; left: 10px; top: 287px; width: 324px; height: 38px; display: flex;
  }
  .notify-form .field {
    flex: 1; border: 1px solid var(--line); border-right: none; border-radius: 2px 0 0 2px;
    padding-left: 8px; display: flex; align-items: center;
    font-size: 10.5px; color: var(--muted); letter-spacing: 0.3px;
  }
  .btn {
    background: var(--brand-red); color: var(--white); border-radius: 2px;
    font-size: 10.5px; letter-spacing: 0.8px; text-transform: uppercase;
    display: flex; align-items: center; justify-content: center;
  }
  .notify-form .btn { width: 81px; border-radius: 0 2px 2px 0; }
  .app-preview {
    position: absolute; left: 394px; top: 63px; width: 138px; height: 278px;
    border-radius: 20px; background: linear-gradient(160deg, #f7f7f7, var(--phone-tone));
    box-shadow: 0 10px 14px -8px rgba(0,0,0,0.25);
  }
  .feature-links {
    position: absolute; left: 71px; top: 389px; display: flex; gap: 23px;
  }
  .feature-links span {
    font-size: 10.5px; letter-spacing: 0.6px; text-transform: uppercase; color: var(--ink);
    padding-bottom: 2px; border-bottom: 1px solid var(--ink);
  }

  /* Right: organizers */
  .organizers {
    position: absolute; left: 600px; top: 91px; width: 600px; height: 475px;
    background: var(--panel);
  }
  .organizers .headline { left: 66px; top: 21px; }
  .organizers .pitch-title { left: 68px; top: 66px; }
  .organizers .pitch-text { left: 68px; top: 101px; width: 245px; }
  .organizers .contact-title { left: 68px; top: 180px; }
  .organizers .contact-text { left: 68px; top: 206px; width: 245px; }
  .team-photo {
    position: absolute; left: 342px; top: 27px; width: 226px; height: 231px;
    background: linear-gradient(180deg, var(--photo-tone-b), var(--photo-tone-a));
  }
  .contact-form .input {
    position: absolute; background: var(--panel); border: 1px solid var(--line); border-radius: 2px;
    font-size: 10.5px; color: var(--muted); letter-spacing: 0.3px; padding: 0 6px;
    display: flex; align-items: center;
  }
  .contact-form .name { left: 68px; top: 275px; width: 221px; height: 33px; }
  .contact-form .email { left: 302px; top: 275px; width: 221px; height: 33px; }
  .contact-form .message {
    left: 68px; top: 322px; width: 455px; height: 57px; align-items: flex-start; padding-top: 6px;
  }
  .contact-form .btn { position: absolute; left: 69px; top: 395px; width: 85px; height: 36px; }

  /* Footer */
  .site-footer {
    position: absolute; left: 0; top: 566px; width: 1200px; height: 59px;
    background: var(--white); box-shadow: 0 -1px 3px rgba(0,0,0,0.06);
  }
  .site-footer .social { left: 12px; top: 18px; }
  .copyright {
    position: absolute; left: 0; width: 1272px; top: 22px; text-align: center;
    font-size: 10.5px; letter-spacing: 0.4px; color: var(--ink);
  }
  .footer-nav {
    position: absolute; right: 10px; top: 22px;
    font-size: 10.5px; letter-spacing: 0.4px; color: var(--ink);
  }
</style>
</head>
<body>
<div class="page">
  <header class="site-header">
    <div class="social" aria-label="Social links"><span></span><span></span><span></span></div>
    <div class="wordmark"><span class="wordmark-dot"></span><span class="wordmark-name">k7ravi</span></div>
    <div class="launch-note">Launching spring 2018</div>
  </header>

  <section class="community">
    <h1 class="headline">Connect your traning, friends, and events in one place.</h1>
    <h2 class="subhead intro-title">A new fitness community is coming soon.</h2>
    <p class="body-copy intro-text">Lorem ipsum dolor sit amet, consectetur adipiscing elit. Aliquam sed hendrerit eros, sit amet bibendum mi. Aliquam orci massa, finibus ac commodo fermentum, placerat faucibus dui.</p>
    <h2 class="subhead signup-title">Join our email list. A referral program is coming and you’ll want to be the first to know.</h2>
    <div class="notify-form">
      <div class="field">Email address</div>
      <div class="btn">Notify me</div>
    </div>
    <div class="app-preview" role="img" aria-label="Mobile phone showing the k7ravi app start screen"></div>
    <nav class="feature-links">
      <span>Sign up for events</span>
      <span>Invite your friends</span>
      <span>Connect your workouts</span>
    </nav>
  </section>

  <section class="organizers">
    <h1 class="headline">Organizing an event?</h1>
    <h2 class="subhead pitch-title">Attaching particiants is hard</h2>
    <p class="body-copy pitch-text">Create your event on k7ravi and we'll handle the registrations, and our team of markating experts will help drive up you participations numbers.</p>
    <h2 class="subhead contact-title">Contact us</h2>
    <p class="body-copy contact-text">Our mission is to drive up participation in endurance events.<br>Let us know how we can help.</p>
    <div class="team-photo" role="img" aria-label="Photo of a smiling team of four event organizers"></div>
    <div class="contact-form">
      <div class="input name">Your Name</div>
      <div class="input email">Email Address</div>
      <div class="input message">How can we help?</div>
      <div class="btn">Send</div>
    </div>
  </section>

  <footer class="site-footer">
    <div class="social" aria-label="Social links"><span></span><span></span><span></span></div>
    <div class="copyright">Copyright © 2018 k7ravi</div>
    <div class="footer-nav">About us | Developers | Careers | Contact</div>
  </footer>
</div>
</body>
</html>
```